Cosmetic Clinic Looking For Sign Designs

We are looking for sign design ideas for the front of our building and a lawn sign for our cosmetic injection salon.
I have uploaded the front of our building for a mock up and size, lawn posts with size and a sign that uses the same dimensions.
We would like both signs to be black for the background.

Target Market(s)

Ages 18-75

Industry/Entity Type

Beauty

Requirements
Must have
• Services we offer:
• Cosmetic Injections
• Airbrush Spray Tanning
• Eyelash Growth Serum
• Skin Care Products & More
• Everything must be on a black background
• The lawn sign must have the address: 394 Fenwick and the building sign should have the phone number.
Should not have
• Nothing can light up (no LED)
• Both signs do not need the full address. Just 394 Fenwick and the phone number

```html
<!DOCTYPE html>
<html lang="en">
<head>
<meta charset="UTF-8">
<title>Bright Hour Studio – Lawn Sign</title>
<link href="https://fonts.googleapis.com/css2?family=Roboto:wght@400;500;700&display=swap" rel="stylesheet">
<style>
  :root {
    --page-bg: #f2f2f2;
    --sign-black: #1d1d20;
    --brand-teal: #1f9cb8;
    --brand-purple: #7d7fc0;
    --text-white: #f4f4f4;
  }
  html, body {
    margin: 0;
    padding: 0;
    width: 1200px;
    height: 1000px;
    overflow: hidden;
    background: var(--page-bg);
  }
  .canvas {
    position: relative;
    width: 1200px;
    height: 1000px;
    display: flex;
    align-items: center;
    justify-content: center;
  }
  .lawn-sign {
    width: 760px;
    height: 700px;
    background: var(--sign-black);
    box-sizing: border-box;
    padding-top: 50px;
    display: flex;
    flex-direction: column;
    align-items: center;
    font-family: "Roboto", sans-serif;
  }
  .brand-mark {
    width: 120px;
    height: 120px;
    display: block;
  }
  .brand-name {
    margin: 26px 0 0;
    font-size: 64px;
    font-weight: 500;
    letter-spacing: 1px;
    color: var(--brand-teal);
    text-transform: uppercase;
    line-height: 1;
  }
  .service-list {
    list-style: none;
    margin: 58px 0 0;
    padding: 0;
    text-align: center;
  }
  .service-list li {
    font-size: 37px;
    font-weight: 400;
    letter-spacing: 0.5px;
    color: var(--text-white);
    line-height: 57px;
  }
  .sign-address {
    margin: 22px 0 0;
    font-size: 42px;
    font-weight: 700;
    color: var(--brand-teal);
  }
</style>
</head>
<body>
  <main class="canvas">
    <section class="lawn-sign">
      <svg class="brand-mark" viewBox="0 0 120 120" aria-hidden="true">
        <circle cx="60" cy="60" r="58" fill="var(--brand-purple)"/>
      </svg>
      <h1 class="brand-name">Bright Hour Studio</h1>
      <ul class="service-list">
        <li>COSMETIC INJECTIONS</li>
        <li>AIRBRUSH SPRAY TANNING</li>
        <li>EYELASH GROWTH SERUM</li>
        <li>SKIN CARE PRODUCTS &amp; MORE</li>
      </ul>
      <p class="sign-address">394 Fenwick Street</p>
    </section>
  </main>
</body>
</html>
```